Lanternfield Advisory logo/business card design -- a digital consulting company

I've just restarted a consulting company I had years ago--Lanternfield Advisory. Now I need a new business card and updated logo. The original logo was simple enough: a chart-like progression atop a grid (see the attached file). I do strategy work, and the chart is meant to show incremental growth and profit. I'd like the reincarnation of my logo to be 3D, with both the grid and arrow rotated on their axis.

I'll want to use the logo on my website as well. I'm open to color schemes, fonts, etc.

Target Market(s)

Business-to-Business. Target market is corporate.

Industry/Entity Type

Business

Contact Information for Business Card

Logo on one-side; name and other contact info on the back

Font styles to use
Serif
Sans Serif

Requirements
Nice to have
• Lanternfield Advisory refers to the concept of "bootstrapping" or making incremental changes to grow with minimal risk and financial exposure, and self-sufficiency (think of the phrase "to pull oneself by one's bootstraps.")

```html
<!DOCTYPE html>
<html lang="en">
<head>
<meta charset="utf-8">
<title>Lanternfield Advisory — Business Card</title>
<link rel="stylesheet" href="https://fonts.googleapis.com/css2?family=Roboto:wght@400;500;700&display=swap">
<style>
  :root {
    --page: #ffffff;
    --red: #d8131b;
    --red-deep: #8e0a0e;
    --grid-core: #120304;
    --silver-light: #e9e9ea;
    --silver-mid: #bfc0c2;
    --silver-dark: #8f9093;
    --ink: #1d1d1f;
    --white: #ffffff;
    --divider: #4a4a4d;
  }
  * { box-sizing: border-box; margin: 0; padding: 0; }
  html, body {
    width: 1200px;
    height: 900px;
    overflow: hidden;
    background: var(--page);
    font-family: "Roboto", Arial, sans-serif;
  }
  .stage {
    position: relative;
    width: 1200px;
    height: 900px;
  }
  .card {
    position: absolute;
    top: 290px;
    width: 540px;
    height: 320px;
    border-radius: 28px;
    overflow: hidden;
    box-shadow: 0 10px 28px rgba(0, 0, 0, 0.18);
  }
  /* Front: logo side */
  .card-front { left: 40px; }
  .front-artwork {
    position: absolute;
    inset: 0;
    background:
      radial-gradient(ellipse 30% 34% at 50% 44%, var(--grid-core) 0%, var(--grid-core) 55%, rgba(18,3,4,0) 100%),
      radial-gradient(ellipse 75% 80% at 50% 46%, var(--red-deep) 0%, var(--red) 70%, #f0262c 100%);
  }
  .front-brand {
    position: absolute;
    left: 0;
    right: 0;
    top: 182px;
    text-align: center;
    color: var(--white);
    font-weight: 500;
    font-size: 38px;
    letter-spacing: 3px;
    text-transform: uppercase;
    line-height: 1;
  }
  /* Back: contact side */
  .card-back { left: 620px; }
  .back-surface {
    position: absolute;
    inset: 0;
    background: linear-gradient(180deg, var(--silver-dark) 0%, var(--silver-light) 46%, var(--silver-mid) 100%);
  }
  .identity {
    position: absolute;
    top: 116px;
    right: 240px;
    text-align: right;
  }
  .identity-name {
    color: var(--red);
    font-size: 20px;
    font-weight: 500;
    line-height: 1.1;
  }
  .identity-role {
    color: var(--ink);
    font-size: 12.5px;
    font-weight: 500;
    margin-top: 4px;
  }
  .divider {
    position: absolute;
    top: 112px;
    left: 308px;
    width: 1px;
    height: 80px;
    background: var(--divider);
  }
  .contact-list {
    position: absolute;
    top: 112px;
    left: 316px;
    list-style: none;
    color: var(--ink);
    font-size: 12px;
    line-height: 16px;
  }
  .contact-list li {
    display: flex;
    align-items: center;
    gap: 4px;
  }
  .contact-list .icon {
    width: 11px;
    height: 11px;
    flex: none;
    fill: var(--red);
  }
  .contact-list .address-line { padding-left: 15px; }
  .back-brand {
    position: absolute;
    right: 22px;
    bottom: 58px;
    display: flex;
    align-items: center;
    gap: 6px;
    color: var(--red);
    font-size: 13px;
    font-weight: 500;
    letter-spacing: 1px;
    text-transform: uppercase;
  }
  .back-brand .mark {
    width: 10px;
    height: 10px;
    background: var(--red);
  }
</style>
</head>
<body>
<main class="stage">
  <section class="card card-front" aria-label="Business card front">
    <div class="front-artwork" role="img" aria-label="Red perspective grid tunnel receding to a dark centre"></div>
    <p class="front-brand">Lanternfield Advisory</p>
  </section>

  <section class="card card-back" aria-label="Business card back">
    <div class="back-surface"></div>

    <div class="identity">
      <p class="identity-name">Name Surname</p>
      <p class="identity-role">CEO &amp; Managing Director</p>
    </div>
    <div class="divider"></div>

    <ul class="contact-list">
      <li>
        <svg class="icon" viewBox="0 0 12 12" aria-hidden="true"><rect x="3" y="0.5" width="6" height="11" rx="1"/><rect x="4" y="2" width="4" height="6" fill="#fff"/></svg>
        1300 482 619
      </li>
      <li>
        <svg class="icon" viewBox="0 0 12 12" aria-hidden="true"><path d="M2.5 0.8 L4.6 3 L3.6 4.4 C4.3 6 5.8 7.6 7.5 8.4 L8.9 7.4 L11.2 9.4 L10 11.2 C5.6 11 1 6.4 0.8 2 Z"/></svg>
        02 7140 2256
      </li>
      <li>
        <svg class="icon" viewBox="0 0 12 12" aria-hidden="true"><rect x="0.5" y="2.5" width="11" height="7.5" rx="0.8"/><path d="M1 3 L6 7 L11 3" fill="none" stroke="#fff" stroke-width="1"/></svg>
        hello@lanternfieldadvisory.com
      </li>
      <li>
        <svg class="icon" viewBox="0 0 12 12" aria-hidden="true"><circle cx="6" cy="6" r="5.5"/><g fill="none" stroke="#fff" stroke-width="0.8"><ellipse cx="6" cy="6" rx="2.2" ry="5.3"/><line x1="0.6" y1="6" x2="11.4" y2="6"/></g></svg>
        www.lanternfieldadvisory.com
      </li>
      <li>
        <svg class="icon" viewBox="0 0 12 12" aria-hidden="true"><path d="M6 0.8 L11.5 5.8 L10 5.8 L10 11.2 L7.3 11.2 L7.3 7.8 L4.7 7.8 L4.7 11.2 L2 11.2 L2 5.8 L0.5 5.8 Z"/></svg>
        Level 4, 118 Carrow Lane
      </li>
      <li class="address-line">Harbourside 2000 NSW</li>
    </ul>

    <p class="back-brand"><span class="mark" aria-hidden="true"></span>Lanternfield Advisory</p>
  </section>
</main>
</body>
</html>
```